Card design for Heating and Cooling company

this is for a heating and cooling company we recently updated our logo and need to update our cards. We attached our logo so you can incorporate it into the card. We specialize in residential and commercial furnace and air condition repairs. Have been in business since 2014.

Phone number 555.284.9137

We need the following phrases
:Repairs, Installations, and maintenance
:Quality work at reasonable prices
:residential/commercial
:Licensed &Insured
:Email Pinegrovehvac47@mailbox-example.com
Name: Teodor K (Ted)
Also on back side I would like my logo with wording :Thank you for your business and refferal

Industry/Entity Type

Hvac

Contact Information for Business Card

:residential/commercial
:Licensed & Insured
Name: Teodor K (Ted)
Number:555.284.9136

Requirements
Must have
• Blue and red colors
Nice to have
• Maybe a pic of a furnace or air conditioner

```html
<!DOCTYPE html>
<html lang="en">
<head>
<meta charset="utf-8">
<title>Pinegrove Heating &amp; Cooling – Business Card</title>
<link rel="stylesheet" href="https://fonts.googleapis.com/css2?family=Tinos:wght@400;700&display=swap">
<style>
  :root {
    --page: #f2f2f2;
    --card: #ffffff;
    --blue: #1f8fd6;
    --blue-light: #7cc4ee;
    --blue-text: #2a8fd0;
    --red: #e5302a;
    --orange: #f07a2a;
    --slate: #5b6f9a;
    --ink: #111111;
    --faint-blue: #cfe3f3;
    --faint-red: #f8d3c4;
  }
  * { margin: 0; padding: 0; box-sizing: border-box; }
  html, body { width: 1200px; height: 1000px; overflow: hidden; }
  body {
    background: var(--page);
    font-family: "Tinos", "Times New Roman", serif;
    position: relative;
  }
  .card {
    position: absolute;
    top: 350px;
    width: 525px;
    height: 300px;
    background: var(--card);
    box-shadow: 0 6px 18px rgba(0,0,0,0.18);
    overflow: hidden;
  }
  .card-front { left: 50px; }
  .card-back { left: 625px; }
  .card-front svg { display: block; }

  .back-bar {
    position: absolute;
    height: 16px;
  }
  .back-bar-top {
    top: 22px; left: 80px; width: 300px;
    background: var(--blue);
    clip-path: polygon(0 0, 100% 0, 96% 100%, 4% 100%);
  }
  .back-bar-bottom {
    bottom: 22px; left: 200px; width: 300px;
    background: var(--red);
    clip-path: polygon(4% 0, 96% 0, 100% 100%, 0 100%);
  }
  .service-list {
    position: absolute;
    list-style: none;
    font-size: 13px;
    color: var(--blue-text);
  }
  .service-list li { display: flex; align-items: center; gap: 8px; margin-bottom: 14px; }
  .service-list-left { top: 58px; left: 22px; }
  .service-list-right { top: 78px; left: 330px; }
  .chevron { width: 9px; height: 12px; flex: none; }
  .back-rule {
    position: absolute;
    top: 150px; left: 20px; right: 20px;
    height: 2px;
    background: var(--blue);
  }
  .contact {
    position: absolute;
    top: 162px; left: 170px;
    color: var(--blue-text);
  }
  .contact-name { font-weight: 700; font-size: 15px; margin-bottom: 12px; }
  .contact-line { display: flex; align-items: center; gap: 10px; font-size: 12px; margin-bottom: 12px; }
  .contact-icon { width: 12px; height: 14px; flex: none; }
  .faint-mark {
    position: absolute;
    width: 70px; height: 70px;
    border-radius: 50%;
  }
  .faint-mark-left { left: 22px; top: 172px; background: var(--faint-blue); }
  .faint-mark-right { right: 40px; top: 200px; background: var(--faint-red); }
</style>
</head>
<body>

  <section class="card card-front" aria-label="Card front">
    <svg width="525" height="300" viewBox="0 0 525 300" xmlns="http://www.w3.org/2000/svg">
      <defs>
        <linearGradient id="cool-tone" x1="0" y1="0" x2="1" y2="1">
          <stop offset="0" stop-color="var(--blue)"/>
          <stop offset="1" stop-color="var(--blue-light)"/>
        </linearGradient>
        <linearGradient id="warm-tone" x1="0" y1="0" x2="1" y2="1">
          <stop offset="0" stop-color="var(--orange)"/>
          <stop offset="1" stop-color="var(--red)"/>
        </linearGradient>
        <linearGradient id="band-tone" x1="0" y1="0" x2="1" y2="0">
          <stop offset="0" stop-color="var(--slate)"/>
          <stop offset="0.6" stop-color="#a04a5a"/>
          <stop offset="1" stop-color="var(--red)"/>
        </linearGradient>
      </defs>
      <rect width="525" height="300" fill="var(--card)"/>
      <path class="cool-decoration" d="M0,0 H300 L290,60 L0,115 Z" fill="url(#cool-tone)" role="img" aria-label="Blue cooling flake decoration"/>
      <path class="warm-decoration" d="M0,270 L525,170 V300 H0 Z" fill="url(#warm-tone)" role="img" aria-label="Orange and red heating flake decoration"/>
      <polygon class="name-band-edge" points="0,212 525,112 525,122 0,222" fill="var(--blue)"/>
      <polygon class="name-band" points="0,226 525,126 525,158 0,258" fill="url(#band-tone)"/>
      <g transform="rotate(-10.8 262 150)">
        <text class="company-name" x="262" y="150" text-anchor="middle" font-family="Tinos, serif" font-weight="700" font-size="38" fill="var(--ink)">PINEGROVE</text>
        <text class="company-sub" x="262" y="170" text-anchor="middle" font-family="Tinos, serif" font-weight="700" font-size="12" letter-spacing="5" fill="var(--ink)">HEATING &amp; COOLING</text>
        <text class="thanks" x="262" y="199" text-anchor="middle" font-family="Tinos, serif" font-size="15" fill="#ffffff">Thank you for your business and refferal</text>
      </g>
    </svg>
  </section>

  <section class="card card-back" aria-label="Card back">
    <div class="back-bar back-bar-top"></div>

    <ul class="service-list service-list-left">
      <li><svg class="chevron" viewBox="0 0 9 12"><path d="M1,1 L7,6 L1,11" fill="none" stroke="var(--blue)" stroke-width="2.5"/></svg>Repairs, Installations, and maintenance</li>
      <li><svg class="chevron" viewBox="0 0 9 12"><path d="M1,1 L7,6 L1,11" fill="none" stroke="var(--blue)" stroke-width="2.5"/></svg>Quality work at reasonable prices</li>
    </ul>
    <ul class="service-list service-list-right">
      <li><svg class="chevron" viewBox="0 0 9 12"><path d="M1,1 L7,6 L1,11" fill="none" stroke="var(--blue)" stroke-width="2.5"/></svg>Residential/commercial</li>
      <li><svg class="chevron" viewBox="0 0 9 12"><path d="M1,1 L7,6 L1,11" fill="none" stroke="var(--blue)" stroke-width="2.5"/></svg>Licensed &amp; Insured</li>
    </ul>

    <div class="back-rule"></div>

    <div class="faint-mark faint-mark-left"></div>
    <div class="faint-mark faint-mark-right"></div>

    <div class="contact">
      <p class="contact-name">TEODOR K (TED)</p>
      <p class="contact-line">
        <svg class="contact-icon" viewBox="0 0 12 14"><rect x="2" y="1" width="8" height="12" rx="1.5" fill="none" stroke="var(--blue)" stroke-width="1.3"/><line x1="5" y1="11" x2="7" y2="11" stroke="var(--blue)" stroke-width="1.2"/></svg>
        555.284.9136
      </p>
      <p class="contact-line">
        <span class="contact-icon" style="font-size:13px;line-height:14px;">@</span>
        Pinegrovehvac47@mailbox-example.com
      </p>
    </div>

    <div class="back-bar back-bar-bottom"></div>
  </section>

</body>
</html>
```